Morvane Estates Business Card and Email Signature Design

I am a Brokiva and need a business card design with my head shot picture and logo and contact information that can be prepared to be used on my email signature as well. I would like my head shot image background to match the background of the business card. So in other words the background of my head shot should be transparent. I would like the Brokiva Logo on there and also MLS and Civic Nestmark Logo. My email address is: lina@morvaneestates.example, Phone Number is: 555-614-7290, website: www.morvaneestates.example Address: 20874 Quillfeather Court Brindlemoor, KS 47518
I also need just the head shot photo with white background in a JPEG file as well so I can upload that picture to my ProfLoop and Hausora profiles.

```html
<!DOCTYPE html>
<html lang="en">
<head>
<meta charset="utf-8">
<title>Morvane Estates Business Card</title>
<link href="https://fonts.googleapis.com/css2?family=Quicksand:wght@400;500;700&display=swap" rel="stylesheet">
<style>
  :root {
    --brand-blue: #1d5b8c;
    --brand-blue-soft: #4a9fd8;
    --ink-dark: #3a3d42;
    --paper: #ffffff;
    --canvas-bg: #e9ecef;
  }
  * { box-sizing: border-box; margin: 0; padding: 0; }
  html, body { width: 1200px; height: 1200px; overflow: hidden; }
  body {
    background: var(--canvas-bg);
    font-family: "Quicksand", Arial, sans-serif;
    position: relative;
  }
  .card {
    position: absolute;
    left: 180px;
    width: 840px;
    height: 480px;
    background: var(--paper);
    overflow: hidden;
    box-shadow: 0 6px 20px rgba(0,0,0,0.15);
  }
  .card--front { top: 80px; }
  .card--back { top: 640px; }

  /* Brand wordmark */
  .brand { position: absolute; text-align: left; }
  .brand__row { display: flex; align-items: center; gap: 14px; }
  .brand__dot {
    width: 40px; height: 40px; border-radius: 50%;
    background: var(--brand-blue);
    flex: none;
  }
  .brand__name {
    font-weight: 700; color: var(--brand-blue);
    text-transform: uppercase; letter-spacing: 2px; white-space: nowrap;
  }
  .brand__tagline {
    font-weight: 700; color: var(--ink-dark);
    text-transform: uppercase; letter-spacing: 5px; white-space: nowrap;
  }

  /* Front */
  .card--front .brand { left: 60px; top: 134px; }
  .card--front .brand__name { font-size: 34px; }
  .card--front .brand__tagline { font-size: 14px; margin: 6px 0 0 56px; }
  .front-band {
    position: absolute; left: 0; right: 0; bottom: 0; height: 190px;
    background: var(--brand-blue);
  }
  .headshot {
    position: absolute; right: 0; bottom: 0; width: 280px; height: 380px;
    background: linear-gradient(180deg, #f3f1ef 0%, #c9b9ab 38%, #3c4450 70%, #2b3340 100%);
  }

  /* Back */
  .back-panel { position: absolute; inset: 0; }
  .back-panel svg { display: block; }
  .contact-name {
    position: absolute; left: 40px; top: 68px;
    color: var(--paper); font-weight: 700; font-size: 34px; white-space: nowrap;
  }
  .contact-role {
    font-size: 18px; font-weight: 500; font-style: italic;
    color: var(--brand-blue-soft); margin-left: 10px;
  }
  .contact-line {
    position: absolute; display: flex; align-items: center; gap: 14px;
    color: var(--brand-blue-soft); font-size: 20px; font-weight: 500; white-space: nowrap;
  }
  .contact-line svg { flex: none; }
  .contact-line--phone { left: 40px; top: 140px; }
  .contact-line--web { left: 40px; top: 190px; }
  .contact-line--address { left: 40px; top: 312px; }
  .contact-line--email { left: 40px; top: 362px; }
  .card--back .brand { left: 466px; top: 112px; }
  .card--back .brand__name { font-size: 26px; }
  .card--back .brand__tagline { font-size: 11px; margin: 6px 0 0 54px; letter-spacing: 4px; }
  .badge-listing {
    position: absolute; left: 40px; top: 244px; width: 70px; height: 22px;
    background: var(--paper); border-radius: 3px;
  }
  .badge-housing {
    position: absolute; right: 36px; bottom: 28px; width: 40px; height: 40px;
    border: 3px solid var(--ink-dark); border-radius: 2px;
  }
</style>
</head>
<body>

<section class="card card--front">
  <div class="front-band"></div>
  <div class="brand">
    <div class="brand__row">
      <span class="brand__dot"></span>
      <span class="brand__name">Morvane Estates</span>
    </div>
    <div class="brand__tagline">Real Estate Services</div>
  </div>
  <div class="headshot" role="img" aria-label="Headshot of the agent in a dark suit and blue shirt, background removed"></div>
</section>

<section class="card card--back">
  <div class="back-panel">
    <svg width="840" height="480" viewBox="0 0 840 480" aria-hidden="true">
      <path d="M0,40 H390 Q420,40 420,70 V250 Q420,280 450,280 H840 V480 H0 Z" fill="var(--brand-blue)"/>
    </svg>
  </div>

  <div class="contact-name">Lina Harrow<span class="contact-role">Brokiva</span></div>

  <div class="contact-line contact-line--phone">
    <svg width="18" height="26" viewBox="0 0 18 26" fill="none" stroke="var(--brand-blue-soft)" stroke-width="2"><rect x="2" y="1" width="14" height="24" rx="2"/><line x1="7" y1="21" x2="11" y2="21"/></svg>
    <span>555-614-7290</span>
  </div>
  <div class="contact-line contact-line--web">
    <svg width="26" height="22" viewBox="0 0 26 22" fill="none" stroke="var(--brand-blue-soft)" stroke-width="2"><rect x="1" y="1" width="24" height="15" rx="1"/><line x1="9" y1="21" x2="17" y2="21"/><line x1="13" y1="16" x2="13" y2="21"/></svg>
    <span>www.morvaneestates.example</span>
  </div>

  <div class="badge-listing" aria-label="Listing service badge"></div>

  <div class="contact-line contact-line--address">
    <svg width="20" height="26" viewBox="0 0 20 26" fill="none" stroke="var(--brand-blue-soft)" stroke-width="2"><path d="M10 25 C10 25 2 15 2 9 A8 8 0 0 1 18 9 C18 15 10 25 10 25 Z"/><circle cx="10" cy="9" r="3"/></svg>
    <span>20874 Quillfeather Court Brindlemoor, KS 47518</span>
  </div>
  <div class="contact-line contact-line--email">
    <svg width="26" height="20" viewBox="0 0 26 20" fill="none" stroke="var(--brand-blue-soft)" stroke-width="2"><rect x="1" y="1" width="24" height="18"/><polyline points="1,1 13,11 25,1"/></svg>
    <span>lina@morvaneestates.example</span>
  </div>

  <div class="brand">
    <div class="brand__row">
      <span class="brand__dot"></span>
      <span class="brand__name">Morvane Estates</span>
    </div>
    <div class="brand__tagline">Real Estate Services</div>
  </div>

  <div class="badge-housing" aria-label="Civic Nestmark badge"></div>
</section>

</body>
</html>
```